I need a logo, business card and letterhead designed. I've just started a Property Management business based in Sydney, Australia. My company name is KLW Management and I would love my name to be combined within the logo, not just two separate images. KLW stands for Kestrel Landholding Works.The focus on my business is great service, although small right now, I believe it will definitely grow over time. I prefer simplicity and don't mind abstract designs, as long as they aren't too abstract. I would like it to convey a sense of professionalism yet a very 'down to earth company'
Updates

Target Market(s)

My service is to all clientele, generally the upper end of the market with investments in property. The age group would be around 35 years old and up. Also the Asian market as well, since I am bilingual in Chinese but the logo doesn't need to reflect that.

Industry/Entity Type

Business

Requirements
Must have
• The logo must still be able to look nice if printed in black and white/greyscale.
Nice to have
• I would love to see my company name combined in the logo. If there was any regency to Australian, I would love that. It could be the colour scheme representing the Australian beach or anything along those lines.
Should not have
• The design cannot be specific to one culture, for example, I don't like having chinese characters or cultural specific items in my logo, in that other people cannot understand it.

```html
<!DOCTYPE html>
<html lang="en">
<head>
<meta charset="utf-8">
<title>KLW Management – Letterhead</title>
<link rel="stylesheet" href="https://fonts.googleapis.com/css2?family=Questrial&display=swap">
<style>
  :root {
    --backdrop: #e4e5e6;
    --paper: #f6f6f6;
    --brand-blue: #1a76a8;
    --band-grey: #6e6e6e;
    --ink: #6a6a6a;
    --ink-soft: #8a8a8a;
    --map-tone: #e6e6e6;
  }
  * { box-sizing: border-box; margin: 0; padding: 0; }
  html, body {
    width: 1200px;
    height: 968px;
    overflow: hidden;
    background: var(--backdrop);
    font-family: "Questrial", "Century Gothic", sans-serif;
  }
  .letterhead {
    position: absolute;
    left: 282px;
    top: 34px;
    width: 636px;
    height: 900px;
    background: var(--paper);
    box-shadow: 0 2px 10px rgba(0,0,0,0.12);
  }
  .brand {
    position: absolute;
    left: 64px;
    top: 58px;
    display: flex;
    align-items: center;
    gap: 10px;
    color: var(--brand-blue);
    font-size: 27px;
    letter-spacing: 0.5px;
  }
  .brand-mark {
    width: 10px;
    height: 10px;
    background: var(--brand-blue);
  }
  .region-map {
    position: absolute;
    left: 110px;
    top: 230px;
    width: 440px;
    height: 470px;
    border-radius: 46% 42% 40% 48% / 40% 44% 52% 46%;
    background: radial-gradient(ellipse at 50% 45%, var(--map-tone) 0%, var(--map-tone) 60%, rgba(230,230,230,0) 100%);
  }
  .contact {
    position: absolute;
    left: 64px;
    bottom: 48px;
    display: flex;
    gap: 34px;
    font-size: 9.5px;
    line-height: 17px;
    color: var(--ink);
  }
  .contact-group { display: flex; flex-direction: column; }
  .contact-item { display: flex; align-items: center; gap: 6px; }
  .contact-icon { width: 10px; height: 10px; flex: none; }
  .contact-address { color: var(--ink-soft); }
  .footer-band {
    position: absolute;
    left: 0;
    right: 0;
    bottom: 0;
    height: 14px;
    display: flex;
  }
  .footer-band-accent { width: 150px; background: var(--brand-blue); }
  .footer-band-base { flex: 1; background: var(--band-grey); }
</style>
</head>
<body>
  <main class="letterhead">
    <header class="brand">
      <span class="brand-mark"></span>
      <span class="brand-name">KLW Management</span>
    </header>

    <div class="region-map" role="img" aria-label="Faint outline map of Australia as a watermark"></div>

    <footer class="contact">
      <div class="contact-group">
        <span class="contact-item">
          <svg class="contact-icon" viewBox="0 0 10 10"><circle cx="5" cy="5" r="5" fill="#1a76a8"/><path d="M3.3 2.6c.3-.2.6-.1.8.2l.4.7c.1.2 0 .4-.2.6l-.3.2c.3.6.8 1.1 1.4 1.4l.2-.3c.2-.2.4-.3.6-.2l.7.4c.3.2.4.5.2.8-.3.5-.8.7-1.3.5C4.5 6.5 3.5 5.5 3 4.2c-.2-.6 0-1.2.3-1.6z" fill="#fff"/></svg>
          +61 2 9400 3150
        </span>
        <span class="contact-item">
          <svg class="contact-icon" viewBox="0 0 10 10"><circle cx="5" cy="5" r="5" fill="#1a76a8"/><rect x="2.5" y="3.5" width="5" height="3.4" rx="0.4" fill="#fff"/><rect x="3.3" y="2.6" width="3.4" height="1.2" fill="#fff"/></svg>
          +61 2 9400 3160
        </span>
      </div>
      <div class="contact-group">
        <span class="contact-item">
          <svg class="contact-icon" viewBox="0 0 10 10"><circle cx="5" cy="5" r="5" fill="#1a76a8"/><rect x="2.4" y="3.2" width="5.2" height="3.6" fill="#fff"/><path d="M2.4 3.2 5 5.2l2.6-2" fill="none" stroke="#1a76a8" stroke-width="0.6"/></svg>
          hello@klwmanagement.com
        </span>
        <span class="contact-item">
          <svg class="contact-icon" viewBox="0 0 10 10"><circle cx="5" cy="5" r="5" fill="#1a76a8"/><circle cx="5" cy="5" r="2.8" fill="none" stroke="#fff" stroke-width="0.6"/><ellipse cx="5" cy="5" rx="1.2" ry="2.8" fill="none" stroke="#fff" stroke-width="0.6"/><path d="M2.2 5h5.6" stroke="#fff" stroke-width="0.6"/></svg>
          www.klwmanagement.com
        </span>
      </div>
      <div class="contact-group contact-address">
        <span>58 Harbourview Lane,</span>
        <span>Kestrel Heights, 2150</span>
      </div>
    </footer>

    <div class="footer-band">
      <span class="footer-band-accent"></span>
      <span class="footer-band-base"></span>
    </div>
  </main>
</body>
</html>
```